Fifty Turning Pages

- Title: FIFTY TURNING PAGES
- Subtitle: 50 Years • 50 Songs • A Lifetime of Memories
- Content: 50 songs (year + artist) listed between 1976–2024 - see attached file for song listing
- Personal dedication: “For the woman who remembers life one song at a time. Happy 50th Birthday — January 2025. With love, Harold.”
- Final size: A2 (420 × 594 mm)
- Style: Elegant, music-themed, typography-led (minimal graphic elements like vinyl / soundwave / gold line accents).
- Deliverables: High-resolution A2 PDF (print-ready), plus source file (Canva/PSD/AI).
- Color preference: Matte palette (black/white/cream/gold accents).
- Target: Framed print quality poster.

```html
<!DOCTYPE html>
<html lang="en">
<head>
<meta charset="utf-8">
<title>Fifty Turning Pages</title>
<link href="https://fonts.googleapis.com/css2?family=Montserrat:wght@300;400;500;600;700;800&display=swap" rel="stylesheet">
<style>
  :root {
    --ink: #141414;
    --paper: #f4efe4;
    --gold: #d2a54f;
    --gold-deep: #a8782a;
    --muted: #9b968c;
    --rule: #3a3631;
  }
  * { margin: 0; padding: 0; box-sizing: border-box; }
  html, body { width: 682px; height: 1200px; overflow: hidden; background: var(--ink); }
  .poster {
    position: relative; width: 682px; height: 1200px; overflow: hidden;
    background: var(--ink); color: var(--paper);
    font-family: "Montserrat", sans-serif;
  }
  .title-kicker {
    position: absolute; left: 40px; top: 44px;
    font-size: 20px; font-weight: 300; letter-spacing: 6px; color: var(--paper);
  }
  .title-main {
    position: absolute; left: 36px; top: 70px;
    font-size: 74px; font-weight: 600; letter-spacing: 3px; line-height: 1;
    background: linear-gradient(100deg, var(--gold-deep), #e8c56f 45%, var(--gold-deep) 75%, #d9b05a);
    -webkit-background-clip: text; background-clip: text; color: transparent;
  }
  .tagline {
    position: absolute; left: 386px; top: 84px;
    border-left: 2px solid var(--gold); padding-left: 14px;
    font-size: 13px; font-weight: 400; letter-spacing: 1.5px; line-height: 21px;
    text-transform: uppercase;
  }
  .divider {
    position: absolute; left: 40px; right: 40px; top: 176px;
    height: 1px; background: var(--gold);
  }
  .dedication {
    position: absolute; left: 386px; top: 194px;
    font-size: 11.5px; letter-spacing: 1px; line-height: 17px; text-transform: uppercase;
  }
  .dedication strong { font-weight: 700; display: block; }
  .dedication span { font-weight: 400; color: var(--paper); }
  .playlist {
    position: absolute; left: 40px; top: 206px; width: 318px;
    list-style: none;
  }
  .track {
    display: flex; align-items: baseline; height: 19px;
    border-bottom: 1px solid var(--rule);
    font-size: 8px; letter-spacing: 0.6px; text-transform: uppercase; line-height: 18px;
  }
  .track-year { width: 34px; color: var(--gold); font-weight: 600; }
  .track-title { flex: 1; font-weight: 600; color: var(--paper); }
  .track-artist { color: var(--muted); font-weight: 400; text-align: right; }
  .birthday-mark {
    position: absolute; left: 370px; top: 240px; width: 312px; height: 960px;
  }
  .birthday-mark text { font-family: "Montserrat", sans-serif; }
</style>
</head>
<body>
<main class="poster">
  <header>
    <div class="title-kicker">FIFTY TURNING</div>
    <h1 class="title-main">PAGES</h1>
    <p class="tagline">50 Years<br>50 Songs<br>A Lifetime of Memories</p>
  </header>
  <div class="divider"></div>
  <p class="dedication"><strong>For the woman who remembers</strong><span>Life one song at a time</span></p>

  <ol class="playlist">
    <li class="track"><span class="track-year">1975</span><span class="track-title">Golden Hour</span><span class="track-artist">Maple Ray</span></li>
    <li class="track"><span class="track-year">1976</span><span class="track-title">Paper Moons</span><span class="track-artist">The Linwoods</span></li>
    <li class="track"><span class="track-year">1977</span><span class="track-title">Slow River</span><span class="track-artist">Ada Brook</span></li>
    <li class="track"><span class="track-year">1978</span><span class="track-title">Neon Hearts</span><span class="track-artist">City Lanterns</span></li>
    <li class="track"><span class="track-year">1979</span><span class="track-title">Velvet Morning</span><span class="track-artist">June Avery</span></li>
    <li class="track"><span class="track-year">1980</span><span class="track-title">Highway Blue</span><span class="track-artist">Marlow Vance</span></li>
    <li class="track"><span class="track-year">1981</span><span class="track-title">Summer Static</span><span class="track-artist">The Tidelines</span></li>
    <li class="track"><span class="track-year">1982</span><span class="track-title">Silver Avenue</span><span class="track-artist">Nora Kell</span></li>
    <li class="track"><span class="track-year">1983</span><span class="track-title">Dancing Shadows</span><span class="track-artist">Echo Parade</span></li>
    <li class="track"><span class="track-year">1984</span><span class="track-title">Midnight Radio</span><span class="track-artist">Cass Ferro</span></li>
    <li class="track"><span class="track-year">1985</span><span class="track-title">Open Windows</span><span class="track-artist">The Harbors</span></li>
    <li class="track"><span class="track-year">1986</span><span class="track-title">Crystal Rain</span><span class="track-artist">Lena Drum</span></li>
    <li class="track"><span class="track-year">1987</span><span class="track-title">Faded Polaroid</span><span class="track-artist">Pale Arcade</span></li>
    <li class="track"><span class="track-year">1988</span><span class="track-title">Sweet Tomorrow</span><span class="track-artist">Ruby Lane</span></li>
    <li class="track"><span class="track-year">1989</span><span class="track-title">Northern Glow</span><span class="track-artist">Owen Marsh</span></li>
    <li class="track"><span class="track-year">1990</span><span class="track-title">Dream Machine</span><span class="track-artist">The Meridians</span></li>
    <li class="track"><span class="track-year">1991</span><span class="track-title">Broken Compass</span><span class="track-artist">Ivy Stone</span></li>
    <li class="track"><span class="track-year">1992</span><span class="track-title">Wild Orchard</span><span class="track-artist">Sam Hollis</span></li>
    <li class="track"><span class="track-year">1993</span><span class="track-title">Quiet Thunder</span><span class="track-artist">Blue Ember</span></li>
    <li class="track"><span class="track-year">1994</span><span class="track-title">Evening Tide</span><span class="track-artist">Clara Wynn</span></li>
    <li class="track"><span class="track-year">1995</span><span class="track-title">Lucky Stars</span><span class="track-artist">The Fieldnotes</span></li>
    <li class="track"><span class="track-year">1996</span><span class="track-title">Paper Planes</span><span class="track-artist">Milo Crest</span></li>
    <li class="track"><span class="track-year">1997</span><span class="track-title">Endless Road</span><span class="track-artist">Vera Lune</span></li>
    <li class="track"><span class="track-year">1998</span><span class="track-title">Sunday Light</span><span class="track-artist">Coastal Kids</span></li>
    <li class="track"><span class="track-year">1999</span><span class="track-title">Millennium Waltz</span><span class="track-artist">Finn Ardent</span></li>
    <li class="track"><span class="track-year">2000</span><span class="track-title">Little Wonders</span><span class="track-artist">Haze Avenue</span></li>
    <li class="track"><span class="track-year">2001</span><span class="track-title">Glass Houses</span><span class="track-artist">Tessa Vale</span></li>
    <li class="track"><span class="track-year">2002</span><span class="track-title">Heartbeat Drive</span><span class="track-artist">The Pilots</span></li>
    <li class="track"><span class="track-year">2003</span><span class="track-title">Falling Softly</span><span class="track-artist">Iris Moon</span></li>
    <li class="track"><span class="track-year">2004</span><span class="track-title">Open Skies</span><span class="track-artist">Jonah Reed</span></li>
    <li class="track"><span class="track-year">2005</span><span class="track-title">Golden Thread</span><span class="track-artist">Luna Harbor</span></li>
    <li class="track"><span class="track-year">2006</span><span class="track-title">City Rain</span><span class="track-artist">Marcus Fay</span></li>
    <li class="track"><span class="track-year">2007</span><span class="track-title">Lantern Song</span><span class="track-artist">The Orchards</span></li>
    <li class="track"><span class="track-year">2008</span><span class="track-title">Brave Again</span><span class="track-artist">Ella Sway</span></li>
    <li class="track"><span class="track-year">2009</span><span class="track-title">Night Swimming</span><span class="track-artist">Arlo Grey</span></li>
    <li class="track"><span class="track-year">2010</span><span class="track-title">Electric Bloom</span><span class="track-artist">Neon Fields</span></li>
    <li class="track"><span class="track-year">2011</span><span class="track-title">Homeward Bound</span><span class="track-artist">Rosa Quill</span></li>
    <li class="track"><span class="track-year">2012</span><span class="track-title">Starlit Road</span><span class="track-artist">The Wanderers</span></li>
    <li class="track"><span class="track-year">2013</span><span class="track-title">Brighter Days</span><span class="track-artist">Kit Monroe</span></li>
    <li class="track"><span class="track-year">2014</span><span class="track-title">Wildflower Heart</span><span class="track-artist">Sage Avery</span></li>
    <li class="track"><span class="track-year">2015</span><span class="track-title">Still Waters</span><span class="track-artist">Theo Lark</span></li>
    <li class="track"><span class="track-year">2016</span><span class="track-title">Gravity Pull</span><span class="track-artist">Nova Reign</span></li>
    <li class="track"><span class="track-year">2017</span><span class="track-title">Slow Dancing</span><span class="track-artist">Juniper Hale</span></li>
    <li class="track"><span class="track-year">2018</span><span class="track-title">Firefly Nights</span><span class="track-artist">The Lowlands</span></li>
    <li class="track"><span class="track-year">2019</span><span class="track-title">Kind Words</span><span class="track-artist">Mae Ellis</span></li>
    <li class="track"><span class="track-year">2020</span><span class="track-title">Window Seat</span><span class="track-artist">Quiet Harbor</span></li>
    <li class="track"><span class="track-year">2021</span><span class="track-title">Paper Hearts</span><span class="track-artist">Lyle Benton</span></li>
    <li class="track"><span class="track-year">2022</span><span class="track-title">Long Weekend</span><span class="track-artist">Opal Rivers</span></li>
    <li class="track"><span class="track-year">2023</span><span class="track-title">Gold Afternoon</span><span class="track-artist">Wren Calloway</span></li>
    <li class="track"><span class="track-year">2024</span><span class="track-title">Fifty Candles</span><span class="track-artist">The Keepsakes</span></li>
  </ol>

  <svg class="birthday-mark" viewBox="0 0 312 960" aria-label="Happy 50th Birthday, January 2025, Harold">
    <defs>
      <linearGradient id="goldFoil" x1="0" y1="0" x2="1" y2="1">
        <stop offset="0" stop-color="#b8872f"/>
        <stop offset="0.35" stop-color="#e6c068"/>
        <stop offset="0.6" stop-color="#a8782a"/>
        <stop offset="0.85" stop-color="#dcb35c"/>
        <stop offset="1" stop-color="#b8872f"/>
      </linearGradient>
    </defs>
    <text class="age-numeral" transform="translate(405 950) rotate(-90)" font-size="520" font-weight="800" fill="url(#goldFoil)" letter-spacing="-20">50</text>
    <text class="greeting-small" transform="translate(62 720) rotate(-90)" font-size="15" font-weight="500" letter-spacing="7" fill="#f4efe4">HAPPY</text>
    <text class="greeting-large" transform="translate(118 720) rotate(-90)" font-size="56" font-weight="700" letter-spacing="2" fill="#f4efe4">BIRTHDAY</text>
    <text class="greeting-date" transform="translate(136 720) rotate(-90)" font-size="11" font-weight="500" letter-spacing="4" fill="#141414">JAN 2025</text>
    <rect class="name-plate" x="84" y="760" width="36" height="120" fill="#141414"/>
    <text class="name-label" transform="translate(110 870) rotate(-90)" font-size="20" font-weight="700" letter-spacing="2" fill="#f4efe4">HAROLD</text>
  </svg>
</main>
</body>
</html>
```